Business Card design for shipping company 'FERNHOLT INTERNATIONAL LTD'

Classic / traditional business card in black Garamond / Times New Roman or similar text for a shipping / marine transport company, containing the following information:

QUOTE

FERNHOLT INTERNATIONAL LTD

MARTIN QUESTEDGE FICS

T: +44 7902 615370
E: cargo@fernholt-example.com

UNQUOTE

Target Market(s)

Marine / Shipping industry

Contact Information for Business Card

FERNHOLT INTERNATIONAL LTD MARTIN QUESTEDGE FICS T: +44 7902 615370 E: cargo@fernholt-example.com

Font styles to use
Serif

Colors

Designer to choose colors to be used in the design.

Requirements
Must have
• Garamond / Times New Roman or similar text in black colour

```html
<!DOCTYPE html>
<html lang="en">
<head>
<meta charset="utf-8">
<title>Fernholt International Ltd — Business Card</title>
<link href="https://fonts.googleapis.com/css2?family=Old+Standard+TT:ital,wght@0,400;0,700;1,400&display=swap" rel="stylesheet">
<style>
  :root {
    --backdrop: #e4e6ec;
    --card: #ffffff;
    --ink: #1b1b1b;
    --rule: #3a3a3a;
  }
  * { margin: 0; padding: 0; box-sizing: border-box; }
  html, body {
    width: 1200px;
    height: 716px;
    overflow: hidden;
    background: var(--backdrop);
  }
  .card {
    position: absolute;
    left: 100px;
    top: 34px;
    width: 1000px;
    height: 648px;
    background: var(--card);
    font-family: "Old Standard TT", "Times New Roman", serif;
    color: var(--ink);
  }
  .frame {
    position: absolute;
    left: 70px;
    top: 70px;
    right: 70px;
    bottom: 70px;
    border: 1.5px solid var(--rule);
  }
  .company {
    position: absolute;
    top: 70px;
    left: 50%;
    transform: translate(-50%, -50%);
    padding: 0 22px;
    background: var(--card);
    font-weight: 700;
    font-size: 29px;
    letter-spacing: 0.03em;
    white-space: nowrap;
    line-height: 1;
  }
  .name-line {
    position: absolute;
    top: 324px;
    left: 0;
    right: 0;
    transform: translateY(-50%);
    text-align: center;
    white-space: nowrap;
    line-height: 1;
  }
  .name {
    font-weight: 700;
    font-size: 54px;
    letter-spacing: 0.01em;
  }
  .credential {
    font-style: italic;
    font-size: 25px;
    letter-spacing: 0.08em;
    margin-left: 8px;
  }
  .contact {
    position: absolute;
    top: 474px;
    left: 0;
    right: 0;
    text-align: center;
    font-size: 28px;
    line-height: 37px;
    font-style: normal;
  }
</style>
</head>
<body>
  <main class="card">
    <div class="frame"></div>
    <h1 class="company">FERNHOLT INTERNATIONAL LTD</h1>
    <p class="name-line"><span class="name">MARTIN QUESTEDGE</span><span class="credential">FICS</span></p>
    <address class="contact">
      <div class="phone">+44 7902 615370</div>
      <div class="email">cargo@fernholt-example.com</div>
    </address>
  </main>
</body>
</html>
```